Harlan Ridge Smokehouse Jamboree's 10th ever event needs a Poster! This Non-Profit is a blast

We need a totally NEW and FUN poster design to promote our tiny Kentucky town which hosts 40,000+ people who come to meet the TV Celebrity BBQ Pitmasters - who smoke meat for their fans. It is all about Beers, Bands, BBQ + Bourbon. We are a family event with Free music all weekend long.

Target Market(s)

People who love Beer, BBQ, Bands and Bourbon

Colors
ec1f27
0555a3

Requirements
Must have
• Please only use original art.
• High energy / Fresh / Young
• Name: Harlan Ridge Smokehouse Jamboree
• 10th ever
• Sept 4+5, 2020
• Bands, Beer, BBQ + Bourbon
• Hosted by: Copperfield Hollow Distillery
• 2817 Marlow Pike Ashby, KY 40198
• $5 admission - FREE MUSIC - FREE Parking
Nice to have
• Please only use original art. Trademarked images and logos will be rejected.

```html
<!DOCTYPE html>
<html lang="en">
<head>
<meta charset="utf-8">
<title>Harlan Ridge Smokehouse Jamboree – Poster</title>
<link rel="stylesheet" href="https://fonts.googleapis.com/css2?family=Metal+Mania&family=Anton&family=Archivo+Black&family=Gochi+Hand&family=Roboto+Condensed:wght@900&display=swap">
<style>
  :root {
    --festival-red: #ec1f27;
    --festival-blue: #0555a3;
    --flame-deep: #e2461b;
    --flame-mid: #f7922a;
    --flame-light: #fdc54a;
    --smoke-dark: #2a2424;
    --sun-yellow: #ffe100;
    --ink: #111111;
    --white: #ffffff;
    --pig-peach: #f6d9b6;
    --overall-slate: #7597b0;
  }
  * { margin: 0; padding: 0; box-sizing: border-box; }
  html, body { width: 927px; height: 1200px; overflow: hidden; background: #ffffff; }
  .poster {
    position: relative;
    width: 927px;
    height: 1200px;
    overflow: hidden;
    background: var(--flame-mid);
  }
  .flame-backdrop {
    position: absolute; inset: 0;
    background:
      linear-gradient(180deg, var(--smoke-dark) 0%, #5a2d1c 22%, var(--flame-deep) 40%, var(--flame-mid) 65%, var(--flame-light) 85%, var(--flame-mid) 100%);
  }
  .mascot-art {
    position: absolute;
    left: 355px; top: 205px;
    width: 620px; height: 1040px;
    border-radius: 46% 30% 0 48% / 30% 20% 0 40%;
    background: linear-gradient(180deg, var(--pig-peach) 0%, var(--pig-peach) 42%, var(--overall-slate) 58%, var(--overall-slate) 100%);
  }
  .headline {
    position: absolute; left: 26px; top: 14px; width: 880px;
    font-family: "Metal Mania", "Pirata One", serif;
    color: var(--white);
    -webkit-text-stroke: 6px var(--festival-red);
    paint-order: stroke fill;
    text-shadow: 4px 4px 0 rgba(0,0,0,0.55);
    line-height: 1.12;
    text-transform: uppercase;
  }
  .headline-line { display: block; white-space: nowrap; }
  .headline-line--top { font-size: 84px; }
  .headline-line--top sup { font-size: 44px; vertical-align: 30px; }
  .headline-line--bottom { font-size: 80px; }
  .event-date {
    position: absolute; left: 28px; top: 256px;
    font-family: "Roboto Condensed", "Arial Narrow", sans-serif;
    font-weight: 900; font-size: 54px; letter-spacing: -1px;
    color: var(--sun-yellow);
    text-shadow: 3px 3px 0 var(--ink);
  }
  .highlights {
    position: absolute; left: 30px; top: 340px;
    font-family: "Gochi Hand", cursive;
    font-size: 72px; line-height: 78px;
    color: var(--white);
    text-shadow: 3px 3px 0 var(--ink), -1px -1px 0 var(--ink);
    letter-spacing: 3px;
  }
  .pitmaster-callout {
    position: absolute; left: 28px; top: 518px;
    font-family: "Anton", "Impact", sans-serif;
    font-size: 84px; line-height: 86px;
    color: var(--festival-red);
    text-transform: uppercase;
    -webkit-text-stroke: 3px var(--white);
    paint-order: stroke fill;
    letter-spacing: -1px;
  }
  .tagline-bar {
    position: absolute; left: 27px; top: 694px;
    width: 611px; height: 62px;
    background: var(--ink);
    display: flex; align-items: center; justify-content: center;
    font-family: "Metal Mania", serif;
    font-size: 40px; color: var(--white);
    text-transform: uppercase; white-space: nowrap;
  }
  .host {
    position: absolute; left: 28px; top: 778px;
    font-family: "Gochi Hand", cursive;
    font-size: 62px; line-height: 70px;
    color: var(--white);
    text-shadow: 3px 3px 0 var(--ink), -1px -1px 0 var(--ink);
  }
  .address {
    position: absolute; left: 28px; top: 1010px;
    font-family: "Archivo Black", "Arial Black", sans-serif;
    font-size: 30px; line-height: 38px;
    color: var(--ink);
  }
  .price {
    position: absolute; left: 590px; top: 845px;
    font-family: "Archivo Black", "Arial Black", sans-serif;
    color: var(--sun-yellow);
    text-shadow: 4px 4px 0 var(--ink);
    -webkit-text-stroke: 2px var(--ink);
    paint-order: stroke fill;
    display: flex; align-items: flex-start;
    line-height: 1;
  }
  .price-symbol { font-size: 96px; margin-top: 22px; }
  .price-whole { font-size: 190px; }
  .price-cents { font-size: 100px; margin-top: 20px; }
  .admission {
    position: absolute; left: 590px; top: 1028px; width: 304px;
    text-align: right;
    font-family: "Archivo Black", "Arial Black", sans-serif;
    font-size: 46px; color: var(--sun-yellow);
    -webkit-text-stroke: 2px var(--ink);
    paint-order: stroke fill;
    text-shadow: 3px 3px 0 var(--ink);
  }
  .perks {
    position: absolute; left: 24px; top: 1092px; width: 880px;
    display: flex; align-items: center; justify-content: space-between;
    font-family: "Metal Mania", serif;
    font-size: 86px;
    color: var(--white);
    -webkit-text-stroke: 6px var(--festival-red);
    paint-order: stroke fill;
    text-shadow: 4px 4px 0 rgba(0,0,0,0.5);
    text-transform: uppercase; white-space: nowrap;
  }
  .perks-divider {
    width: 10px; height: 52px;
    background: var(--white);
    border: 3px solid var(--festival-red);
  }
</style>
</head>
<body>
<main class="poster">
  <div class="flame-backdrop" role="img" aria-label="Illustrated wall of orange, red and yellow flames over dark smoke swirls"></div>
  <div class="mascot-art" role="img" aria-label="Cartoon pig mascot in blue overalls, smiling with eyes closed"></div>

  <h1 class="headline">
    <span class="headline-line headline-line--top">10<sup>th</sup> Ever Harlan Ridge</span>
    <span class="headline-line headline-line--bottom">Smokehouse Jamboree</span>
  </h1>

  <p class="event-date">SEPTEMBER 4 &amp; 5, 2020</p>

  <p class="highlights">BANDS • BEER<br>BBQ • BOURBON</p>

  <h2 class="pitmaster-callout">Meet TV Celebrity<br>BBQ Pitmasters</h2>
  <p class="tagline-bar">Who smoke meat for their fans</p>

  <p class="host">Hosted by<br>Copperfield Hollow<br>Distillery</p>

  <address class="address" style="font-style:normal">2817 Marlow Pike<br>Ashby, KY 40198</address>

  <p class="price"><span class="price-symbol">$</span><span class="price-whole">5</span><span class="price-cents">00</span></p>
  <p class="admission">ADMISSION</p>

  <p class="perks"><span>Free Music</span><span class="perks-divider"></span><span>Free Parking</span></p>
</main>
</body>
</html>
```